Luxury Ayurvedic Hair Oil logo and package design

We need a logo and package design for our Ayurvedic and natural hair growth oil. Our company, Velmora, is the premier luxury Ayurvedic beauty brand, bringing ancient East-Indian natural and botanic health and beauty products to the US market. Our first major product - Velmora Hair Growth Oil - is a coconut oil based product that was developed by tribes in the Southern State of Kerala that includes ancient herbs like Gooseberry, Indigo, Indian Aloe, Balloon Vine and Brahmi.

The design should be catered to the high-end luxury market (minimal design, minimal text, fonts that invoke a sense of luxury). The primary colors should be deep blue for the packaging and gold for the characters (it's in the name - Velmora). We are looking to sell our products in Lumerelle and Harwick Dunley and require packaging that is in line with products sold at these high-end retailers.

The final logo design and packaging should communicate luxury and the ancient wisdom of far-eastern traditions.

Target Market(s)

Velmora's main target is women who value fashionable/quality skincare, beauty, and fragrance products and are open to a medium to high price range. These women love uniqueness in brand and products that cannot be found elsewhere. They are looking for the next new "it" item that will take their haircare and beauty regiment to the next level.

Industry/Entity Type

Hair And Beauty

Font styles to use
Serif

Colors
2f73b3
ffc214

Requirements
Must have
• Must use deep blue (royal blue) background and gold text (to align with brand name). Must use luxurious fonts
Nice to have
• Flowers or other natural symbols, pictures that blend well with the product theme

```html
<!DOCTYPE html>
<html lang="en">
<head>
<meta charset="utf-8">
<title>Velmora Hair Growth Oil – Label Designs</title>
<link href="https://fonts.googleapis.com/css2?family=Marcellus&display=swap" rel="stylesheet">
<style>
  :root{
    --navy:#0d1636;
    --gold:#e7aa63;
    --gold-soft:#c88f4f;
    --paper:#ebebeb;
    --paper-edge:#dcdcdc;
  }
  *{margin:0;padding:0;box-sizing:border-box}
  html,body{width:1200px;height:1200px;overflow:hidden}
  body{
    background:radial-gradient(ellipse at 40% 30%,#f5f5f5 0%,var(--paper) 60%,var(--paper-edge) 100%);
    font-family:"Marcellus",serif;
    color:var(--gold);
    position:relative;
  }
  .label{
    position:absolute;left:120px;width:960px;
    background:var(--navy);
    box-shadow:10px 12px 14px rgba(0,0,0,.35);
  }
  .label--wrap{top:120px;height:533px;overflow:hidden}
  .label--flat{top:707px;height:373px}
  .abs{position:absolute}
  .center{text-align:center}

  /* wrap label */
  .wrap-directions{left:25px;top:38px;width:162px;font-size:12px;line-height:15.8px}
  .wrap-directions h3{font-weight:400;font-size:12px;margin-bottom:10px}
  .wrap-directions p{margin-bottom:9px}
  .wrap-ingredients{left:25px;top:266px;width:162px;font-size:12px}
  .brand-block{left:246px;top:58px;width:200px}
  .brand-mark{display:block;margin:0 auto 14px;width:34px;height:34px;border:1.5px solid var(--gold);border-radius:50%}
  .brand-name{font-size:22px;letter-spacing:1px;line-height:1}
  .product-title{font-size:35px;line-height:41px;margin-top:18px}
  .product-base{font-size:19px;line-height:22px;margin-top:52px}
  .art-coconut{left:184px;top:334px;width:386px;height:199px;
    background:radial-gradient(ellipse at 45% 85%,rgba(231,170,99,.55) 0%,rgba(231,170,99,.22) 45%,rgba(231,170,99,0) 75%)}
  .art-follicle{left:529px;top:60px;width:112px;height:100px;
    background:radial-gradient(ellipse at 50% 60%,rgba(231,170,99,.4) 0%,rgba(231,170,99,0) 70%)}
  .tagline{left:486px;top:193px;width:200px;font-size:14px;line-height:18px}
  .story{left:710px;top:36px;width:228px;font-size:15px;line-height:19.2px}
  .art-herbs{left:708px;top:296px;width:220px;height:137px;
    background:radial-gradient(ellipse at 55% 60%,rgba(231,170,99,.5) 0%,rgba(231,170,99,.18) 50%,rgba(231,170,99,0) 78%)}
  .volume-wrap{left:724px;top:470px;width:200px;font-size:25px}
  .contact{left:25px;top:375px;font-size:12px;line-height:20px}
  .contact li{list-style:none;display:flex;align-items:center;gap:8px}
  .contact-dot{width:13px;height:13px;border:1.3px solid var(--gold);border-radius:50%}
  .maker{left:25px;top:422px;font-size:12.5px;line-height:18.7px}

  /* flat label */
  .flat-directions{left:27px;top:38px;width:292px}
  .flat-directions h3{font-weight:400;font-size:19px;margin-bottom:12px}
  .flat-directions p{font-size:18.6px;line-height:23.6px;margin-bottom:10px}
  .flat-brand{left:379px;top:28px;width:200px}
  .flat-brand .brand-mark{margin-bottom:14px}
  .flat-brand .product-title{font-size:37px;line-height:42px;margin-top:18px}
  .flat-brand .product-base{font-size:22px;line-height:27px;margin-top:8px}
  .flat-volume{font-size:25px;margin-top:18px}
  .flat-ingredients{left:640px;top:38px;font-size:19px}
  .flat-maker{left:640px;top:249px;font-size:17px;line-height:21.5px}
</style>
</head>
<body>

<section class="label label--wrap" aria-label="Wrap-around bottle label">
  <div class="abs wrap-directions center">
    <h3>Directions:</h3>
    <p>Massage a small amount of oil onto scalp and throughout hair. Leave in hair for at least five minutes or overnight for best results. Rinse and repeat daily.</p>
    <p>For dry scalps and braided hair, apply small amount of oil directly to the scalp for moisture and protection.</p>
  </div>
  <div class="abs wrap-ingredients center">Ingredients:</div>

  <div class="abs brand-block center">
    <span class="brand-mark" aria-hidden="true"></span>
    <div class="brand-name">VELMORA</div>
    <h1 class="product-title" style="font-weight:400">Hair Growth<br>Oil</h1>
    <div class="product-base">Coconut Oil<br>Based</div>
  </div>

  <div class="abs art-coconut" role="img" aria-label="Gold line engraving of coconuts among palm fronds"></div>

  <div class="abs art-follicle" role="img" aria-label="Gold line icon of a hair strand rising from the scalp with sparkles"></div>
  <p class="abs tagline center">To help regrow hair.<br>Stronger, thicker,<br>and healthier hair.</p>

  <p class="abs story center">A divine hair nurturing oil steeped in tribal traditions for creating and maintaining a long, luxurious mane. Developed using ancient ayurvedic methods, Velmora Hair Oil combines Gooseberry, Indian Aloe, Indian Tinospora, Brahmi, and other ingredients in a 100% natural coconut oil base. Feed your hair and allow it room to grow.</p>
  <div class="abs art-herbs" role="img" aria-label="Gold line engraving of aloe leaves, gooseberries and herb sprigs"></div>
  <div class="abs volume-wrap center">50ml</div>

  <ul class="abs contact">
    <li><span class="contact-dot" aria-hidden="true"></span>velmora_beauty</li>
    <li><span class="contact-dot" aria-hidden="true"></span>www.velmorabeauty.com</li>
  </ul>
  <p class="abs maker">Manufacturing:<br>Dist. By Corvane Analytics, LLC,<br>New York<br>Oil made in India</p>
</section>

<section class="label label--flat" aria-label="Front bottle label">
  <div class="abs flat-directions">
    <h3>Directions:</h3>
    <p>Massage a small amount of oil onto scalp and throughout hair. Leave in hair for at least five minutes or overnight for best results. Rinse and repeat daily.</p>
    <p>For dry scalps and braided hair, apply small amount of oil directly to the scalp for moisture and protection.</p>
  </div>

  <div class="abs flat-brand center">
    <span class="brand-mark" aria-hidden="true"></span>
    <div class="brand-name">VELMORA</div>
    <h2 class="product-title" style="font-weight:400">Hair Growth<br>Oil</h2>
    <div class="product-base">Coconut Oil<br>Based</div>
    <div class="flat-volume">50ml</div>
  </div>

  <div class="abs flat-ingredients">Ingredients:</div>
  <p class="abs flat-maker">Manufacturing:<br>Dist. By Corvane Analytics, LLC,<br>New York<br>Oil made in India</p>
</section>

</body>
</html>
```